17 Ways Your Nest Egg Can Bloom Book Cover

I need a book cover for a softcover book I will market directly.
The name of the book will be.
"17 Ways Your Nest Egg Can Bloom!"

I'm open to any and all ideas. But I want the book cover to stand out, to draw people's interest. But feel free to use your skill set to come up with good ideas.

I will be selling this book door to door and onine as well.

Target Market(s)

45-60 year old married couples

Industry/Entity Type

Financial Planning

Colors

Designer to choose colors to be used in the design.

Requirements
Must have
• website address.
• www.lanternoakadvisors.com
Nice to have
• like to have my picture on the back cover, with my company logo too if possible.

```html
<!DOCTYPE html>
<html lang="en">
<head>
<meta charset="utf-8">
<title>17 Ways Your Nest Egg Can Bloom – Cover</title>
<link rel="stylesheet" href="https://fonts.googleapis.com/css2?family=Cinzel:wght@400;500&family=Sorts+Mill+Goudy&family=EB+Garamond:wght@400;600&display=swap">
<style>
  :root {
    --paper: #ffffff;
    --ink: #111111;
    --soft-ink: #2a2a2a;
    --brand: #5aa3a8;
    --bar: #eef0f1;
    --bar-edge: #d4d8da;
    --growth: #6fd31c;
    --photo-top: #c9cdd0;
    --photo-bottom: #7f8488;
  }
  * { margin: 0; padding: 0; box-sizing: border-box; }
  html, body { width: 1200px; height: 915px; overflow: hidden; background: var(--paper); }
  .cover { position: relative; width: 1200px; height: 915px; background: var(--paper); color: var(--ink); }

  /* Back cover */
  .benefits { position: absolute; left: 62px; top: 112px; width: 470px; list-style: none;
    font-family: "Sorts Mill Goudy", serif; font-size: 17.5px; line-height: 21px; }
  .benefits li { position: relative; padding-left: 15px; }
  .benefits li::before { content: "\2605"; position: absolute; left: 0; top: 0; font-size: 11px; }
  .back-rule { position: absolute; left: 0; top: 372px; width: 490px; height: 4px; background: var(--ink); }
  .author-photo { position: absolute; left: 19px; top: 324px; width: 170px; height: 273px;
    background: linear-gradient(180deg, var(--photo-top), var(--photo-bottom)); }
  .bio { position: absolute; left: 216px; top: 394px; width: 280px;
    font-family: "EB Garamond", serif; font-size: 14.5px; line-height: 18px; color: var(--soft-ink); }
  .bio p + p { margin-top: 18px; }
  .company { position: absolute; left: 48px; top: 740px; display: flex; align-items: center; gap: 8px; }
  .company-dot { width: 30px; height: 30px; border-radius: 50%; background: var(--brand); }
  .company-name { font-family: "EB Garamond", serif; font-size: 17px; color: var(--brand); letter-spacing: 0.5px; }

  /* Spine */
  .spine-title, .spine-author { position: absolute; writing-mode: vertical-rl; font-family: "Cinzel", serif; color: var(--ink); }
  .spine-title { left: 589px; top: 172px; font-size: 13px; }
  .spine-author { left: 591px; top: 510px; font-size: 10px; letter-spacing: 6px; }

  /* Front cover */
  .front-rule { position: absolute; left: 796px; top: 120px; width: 404px; height: 4px; background: var(--ink); }
  .title { position: absolute; left: 650px; top: 96px; font-family: "Cinzel", serif; font-weight: 400; color: var(--ink); }
  .title-line { display: block; white-space: nowrap; }
  .title-number { font-size: 172px; line-height: 130px; letter-spacing: -8px; }
  .title-word { font-size: 64px; }
  .line-1 { display: flex; align-items: flex-end; }
  .line-1 .title-word { margin-left: 14px; line-height: 52px; }
  .line-2 { font-size: 64px; line-height: 80px; margin-top: 4px; }
  .line-3 { font-size: 76px; line-height: 92px; }
  .chart { position: absolute; left: 680px; top: 340px; }
  .author-front { position: absolute; left: 680px; top: 778px; font-family: "Cinzel", serif; font-size: 29px; letter-spacing: 15px; }
  .website { position: absolute; left: 752px; top: 830px; font-family: "EB Garamond", serif; font-weight: 600; font-size: 19.5px; }
</style>
</head>
<body>
<main class="cover">
  <!-- back -->
  <ul class="benefits">
    <li>REDUCE income taxes for you, your surviving spouse and your heirs.</li>
    <li>ELIMINATE Social Security taxes for you and your surviving spouse</li>
    <li>AVOID increased Medicare premiums for you and your surviving spouse</li>
    <li>LEAVE a Tax-FREE Legacy to your surviving spouse and heirs</li>
    <li>and much, MUCH more!</li>
  </ul>
  <div class="back-rule"></div>
  <div class="author-photo" role="img" aria-label="Portrait of the author in a grey suit"></div>
  <div class="bio">
    <p>Marcus Ellery is a CERTIFIED FINANCIAL PLANNER Practitioner and holds a Master's of Science degree in Personal Financial Planning.</p>
    <p>Marcus has provided financial advice to clients since 1998. Over those 2 decades he has developed extensive knowledge of investment management, Social Security, tax, retirement planning and wealth transfer strategies.</p>
    <p>He has learned that successful financial planning does not need to be complex. He follows the tried and true rule he learned in the Army, "Keep It Simple, Stupid." In fact, complexity can be the enemy of successful financial planning.</p>
  </div>
  <div class="company">
    <span class="company-dot"></span>
    <span class="company-name">Lantern Oak Advisors</span>
  </div>

  <!-- spine -->
  <div class="spine-title">17 Ways Your Nest Egg Can Bloom</div>
  <div class="spine-author">MARCUS ELLERY</div>

  <!-- front -->
  <div class="front-rule"></div>
  <h1 class="title">
    <span class="title-line line-1"><span class="title-number">17</span><span class="title-word">Ways</span></span>
    <span class="title-line line-2">Your Nest Egg</span>
    <span class="title-line line-3">Can Bloom</span>
  </h1>
  <svg class="chart" width="470" height="400" viewBox="0 0 470 400" aria-hidden="true">
    <ellipse cx="230" cy="372" rx="230" ry="14" fill="#f1f1f1"/>
    <g fill="var(--bar)" stroke="var(--bar-edge)" stroke-width="1">
      <rect x="8" y="322" width="48" height="48"/>
      <rect x="60" y="298" width="48" height="72"/>
      <rect x="112" y="268" width="48" height="102"/>
      <rect x="164" y="232" width="48" height="138"/>
      <rect x="216" y="190" width="48" height="180"/>
      <rect x="268" y="148" width="48" height="222"/>
      <rect x="320" y="108" width="48" height="262"/>
      <rect x="372" y="88" width="40" height="282"/>
      <rect x="416" y="12" width="34" height="358"/>
    </g>
    <polyline points="70,360 140,280 200,300 290,210 340,222 410,138 440,110" fill="none" stroke="var(--growth)" stroke-width="12" stroke-linejoin="round"/>
    <polygon points="422,104 462,84 452,128" fill="var(--growth)"/>
  </svg>
  <div class="author-front">MARCUS ELLERY</div>
  <div class="website">www.lanternoakadvisors.com</div>
</main>
</body>
</html>
```